Inspire Design with Natural Stone: Quarrell Ltd. Tradeshow Booth Backdrop

Client: Quarrell Ltd.
Project Goal: To design a visually compelling and informative 7.5ft x 10ft backdrop for Quarrell Ltd.'s 10ft x 10ft tradeshow booth that attracts and engages architects, designers, homeowners, and contractors, ultimately driving interest in their natural stone products.
Quarrell Ltd. is a leading provider of high-quality natural stone for a wide range of residential and commercial projects. We offer a diverse selection of stone types, finishes, and applications, known for their beauty, durability, and timeless appeal. We are participating in upcoming tradeshows to generate new leads, strengthen brand awareness, and showcase our latest offerings to key target audiences.
Target Audience(s):
Architects: Seeking premium, unique, and sustainable natural stone options for their designs, with an appreciation for quality and aesthetic integration.
Designers (Interior & Landscape): Looking for visually appealing and versatile stone to enhance their projects, focusing on texture, color palettes, and application possibilities.
Homeowners: Aspiring to elevate their living spaces with natural stone, driven by aesthetics, durability, and adding lasting value to their homes.
Contractors: Seeking reliable and high-quality stone suppliers for their building and renovation projects, prioritizing ease of installation and client satisfaction.
Key Message/Desired Outcome: We want our booth to communicate that Quarrell Ltd. is the premier source for beautiful, high-quality natural stone solutions for any project, backed by expertise and a commitment to customer satisfaction. We want to inspire visitors with the possibilities of using natural stone in their designs and projects.
Mandatories:
* Backdrop Dimensions: 7.5 feet (height) x 10 feet (width). (See attached template)
* Inclusion of Quarrell Ltd. Logo:* The logo must be prominently featured and easily recognizable. Please refer to the attached brand guidelines for logo usage, color palette, and typography.
*Clear Representation of Natural Stone: The design must showcase the beauty and variety of Quarrell Ltd.'s natural stone products. This can be achieved through high-quality photography, subtle textures, or artistic representations. Please use our website's photo and project gallery.
*Contact Information: Include our website address: www.quarrellbrix.example
Optional Elements (Consideration):
*Visuals of Applications: Showcasing natural stone used in various settings (e.g., fireplaces, facades, patios, interior walls) could be impactful.
*Highlighting Key Benefits: Briefly communicating the advantages of natural stone (e.g., durability, sustainability, timelessness).
*Integration of Textures: Subtly incorporating textures that hint at the feel of natural stone.
Look and Feel:
*Overall Impression: Sophisticated, natural, high-quality, inviting, trustworthy, and inspiring.
*Style: Clean, modern, and visually appealing, allowing the beauty of the stone to take center stage. Avoid overly busy or cluttered designs.
*Color Palette: Primarily utilize Quarrell Ltd.'s brand colors (refer to brand guidelines).
Things to Avoid:
* Generic stock imagery that doesn't accurately represent Quarrell's products.
* Cluttered layouts with excessive text.
* Designs that appear cheap or unprofessional.
* Difficult-to-read fonts or color combinations.
Deliverables:
* High-resolution digital design file(s) suitable for large-format printing (AI, Photoshop, PDF).
* Mockup of the backdrop design within a 10ft x 10ft booth space. Please feel free to include any other booth features (tables, flooring, etc) that you think would work well with the backdrop (optional but highly recommended).
We are excited to see your creative interpretations and look forward to selecting a design that will make a strong and lasting impression at our upcoming tradeshows!

```html
<!DOCTYPE html>
<html lang="en">
<head>
<meta charset="utf-8">
<title>Quarrell Ltd. – Tradeshow Backdrop</title>
<link rel="stylesheet" href="https://fonts.googleapis.com/css2?family=Questrial&family=Roboto+Condensed:wght@700&display=swap">
<style>
  :root {
    --stage: #d9d9d9;
    --navy: #2c3342;
    --navy-deep: #232936;
    --stone-grey: #8b8c8e;
    --stone-grey-light: #9a9b9d;
    --white: #ffffff;
    --sand: #d6ccb1;
    --mist: #c9cdd4;
  }
  html, body {
    margin: 0;
    padding: 0;
    width: 1200px;
    height: 2700px;
    overflow: hidden;
    background: var(--stage);
  }
  .backdrop {
    position: absolute;
    left: 100px;
    top: 645px;
    width: 1000px;
    height: 1412px;
    display: block;
  }
  .brand-name { font-family: "Questrial", sans-serif; font-size: 26px; fill: var(--white); letter-spacing: 0.5px; }
  .brand-tagline { font-family: "Questrial", sans-serif; font-size: 5.6px; fill: var(--white); letter-spacing: 0.2px; }
  .headline-small { font-family: "Questrial", sans-serif; font-size: 8px; fill: var(--mist); letter-spacing: 0.6px; }
  .headline-large { font-family: "Roboto Condensed", sans-serif; font-weight: 700; font-size: 21px; fill: var(--sand); }
  .web-address { font-family: "Questrial", sans-serif; font-size: 12px; fill: var(--white); }
</style>
</head>
<body>
<svg class="backdrop" viewBox="0 0 340 480" xmlns="http://www.w3.org/2000/svg">
  <defs>
    <radialGradient id="fireplace-tones" cx="50%" cy="55%" r="60%">
      <stop offset="0" stop-color="#b8782f"/>
      <stop offset="0.35" stop-color="#9a8b72"/>
      <stop offset="1" stop-color="#6e6454"/>
    </radialGradient>
    <linearGradient id="wall-tones" x1="0" y1="0" x2="0" y2="1">
      <stop offset="0" stop-color="#8f9a86"/>
      <stop offset="0.55" stop-color="#d4cfc4"/>
      <stop offset="1" stop-color="#6f7174"/>
    </linearGradient>
    <linearGradient id="facade-tones" x1="0" y1="0" x2="1" y2="1">
      <stop offset="0" stop-color="#c9d3df"/>
      <stop offset="1" stop-color="#4b5564"/>
    </linearGradient>
    <linearGradient id="interior-tones" x1="0" y1="0" x2="0" y2="1">
      <stop offset="0" stop-color="#f1f1ef"/>
      <stop offset="0.7" stop-color="#d8d4cd"/>
      <stop offset="1" stop-color="#8a8178"/>
    </linearGradient>
  </defs>

  <!-- base -->
  <rect class="panel-base" width="340" height="480" fill="var(--navy)"/>

  <!-- brand block -->
  <text class="brand-name" x="22" y="92">Quarrell Ltd.</text>
  <text class="brand-tagline" x="27" y="124">~ DURABILITY ~ SUSTAINABILITY ~ TIMELESSNESS</text>

  <!-- headline -->
  <text class="headline-small" x="320" y="58" text-anchor="end">CRAFT YOUR VISION</text>
  <text class="headline-large" x="320" y="78" text-anchor="end">In Stone</text>

  <!-- grey stone wave -->
  <path class="stone-wave" fill="var(--stone-grey)"
        d="M0,205 C70,200 110,150 175,130 C240,112 300,110 340,102 L340,330 C290,322 240,320 180,340 C110,362 50,330 0,318 Z"/>
  <!-- white swoosh on wave top -->
  <path class="swoosh" fill="var(--white)"
        d="M0,198 C70,194 110,142 175,122 C240,104 300,100 340,94 L340,101 C300,108 240,112 175,130 C110,150 70,202 0,207 Z"/>
  <path class="swoosh-thin" fill="none" stroke="var(--white)" stroke-width="2"
        d="M0,215 C50,218 80,200 110,180"/>

  <!-- lower dark bands -->
  <path class="band-deep" fill="var(--navy-deep)"
        d="M0,330 C60,350 120,375 190,352 C250,332 300,328 340,330 L340,372 C280,368 220,380 160,400 C100,418 40,400 0,380 Z"/>
  <path class="band-sand" fill="var(--sand)"
        d="M190,372 C250,356 300,352 340,354 L340,362 C300,360 250,364 196,380 Z"/>
  <path class="band-grey" fill="var(--stone-grey-light)"
        d="M200,392 C260,378 305,375 340,378 L340,390 C300,388 262,392 206,404 Z"/>
  <path class="swoosh-bottom" fill="var(--white)"
        d="M0,372 C40,420 120,440 200,432 C260,426 305,440 340,452 L340,446 C300,432 260,418 200,424 C120,432 50,410 0,362 Z"/>
  <path class="swoosh-bottom-thin" fill="none" stroke="var(--white)" stroke-width="1.5"
        d="M0,395 C50,440 130,452 210,446"/>

  <!-- project photo circles -->
  <circle cx="120" cy="312" r="96" fill="var(--navy-deep)"/>
  <circle cx="120" cy="312" r="92" fill="url(#fireplace-tones)" role="img" aria-label="Stacked stone fireplace with wood mantel in a living room"/>
  <circle cx="213" cy="184" r="49" fill="var(--navy-deep)"/>
  <circle cx="213" cy="184" r="46" fill="url(#wall-tones)" role="img" aria-label="Curved stone retaining wall in a garden"/>
  <circle cx="300" cy="184" r="28" fill="var(--navy-deep)"/>
  <circle cx="300" cy="184" r="25" fill="url(#facade-tones)" role="img" aria-label="Stone home facade with garage door"/>
  <circle cx="290" cy="275" r="49" fill="var(--navy-deep)"/>
  <circle cx="290" cy="275" r="46" fill="url(#interior-tones)" role="img" aria-label="Bright living room with stone fireplace wall"/>

  <!-- contact -->
  <text class="web-address" x="22" y="463">www.quarrellbrix.example</text>
</svg>
</body>
</html>
```